Landing page for new software as a service product

==== ENGLISH VERSION ====

Due to our excellent customer service, the company FernHaven has gained many satisfied customers. Now we have developed a new product, which enables companies in times of Covid-19 to use a video salesroom, to get in contact with their customers. In contrast to many other solutions on the market, it is not only an outbound solution. Our solution can handle incoming calls from the website / shop / app of a customer. The video call is routed by different rules (regarding day of week, time and sales agent) to the correct sales agent. If no sales agent is available different exit strategies are available to not loose the lead.

We need a LANDING PAGE for this application (no backend design!), Which can later be translated into different languages. Attached are screenshots of the application, which can be used if required. If you need other information, you are free to contact us and we try to provide these information to you.

==== GERMAN VERSION ====

As a cloud provider, FernHaven has gained many satisfied customers through excellent customer service in recent years. Now we have developed a new product that enables companies to make sales via video. And not just in the outbound, as known from well-known providers, but also in the inbound. This means that the customer can start a video call to the dealer using a button on the homepage. The call is then routed to the appropriate employee as with a correct telephone system according to previously defined rules (date, time, user groups).

For this application we need a landing page, which can later be translated into other languages. Screenshots of the application are included and additional ones can be created if required. As a technician, it is difficult for us to select the correct information here. So if there is a need for more information, we can certainly provide it if it is named.
Updates

I've made the mistake and made only a german briefing, which was really not suitable for the most designers. I've fixed this error and translated the briefing now.

Requirements
Must have
• A landing page design, for the new product. Please only designs which fits the topic and not some generic designs which need to be customized by us ... If we we're able to do this, we would not ask for help here ;-)
Should not have
• We do not need an admin template for the application, we already have an admin design.

```html
<!DOCTYPE html>
<html lang="en">
<head>
<meta charset="utf-8">
<title>FernHaven – Video Salesroom</title>
<link href="https://fonts.googleapis.com/css2?family=Rubik:wght@300;400;500;700&display=swap" rel="stylesheet">
<style>
:root{
  --ink:#222;
  --muted:#777;
  --dark:#2b2b2b;
  --darker:#232323;
  --white:#fff;
  --pink:#f0506e;
  --blue:#2a9fd6;
  --blue-deep:#1d7ea8;
  --blue-light:#4fb3dc;
  --field:#f3f3f3;
}
*{box-sizing:border-box;margin:0;padding:0}
html,body{width:1200px;height:3446px;overflow:hidden}
body{font-family:"Rubik",sans-serif;color:var(--ink);background:var(--white);position:relative}
section,footer{position:absolute;left:0;width:1200px}

/* hero */
.hero{top:0;height:675px;overflow:hidden}
.hero-photo{position:absolute;inset:0;background:linear-gradient(135deg,#3a4550 0%,#596570 35%,#2e3640 70%,#444c55 100%)}
.hero-shade{position:absolute;inset:0;background:rgba(20,25,30,.45)}
.hero-inner{position:relative;text-align:center;color:var(--white)}
.brand{position:absolute;top:150px;left:0;width:1200px;font-size:84px;font-weight:500;letter-spacing:1px}
.hero-text{position:absolute;top:322px;left:225px;width:750px;font-size:21px;font-weight:300;line-height:1.4}
.hero-actions{position:absolute;top:450px;left:0;width:1200px;display:flex;justify-content:center;gap:28px}
.btn{display:inline-flex;align-items:center;justify-content:center;width:222px;height:66px;border-radius:33px;font-size:18px;font-weight:500;letter-spacing:1px;text-transform:uppercase;color:var(--white)}
.btn-primary{background:var(--pink)}
.btn-ghost{border:2px solid var(--white)}
.hero-arrow{position:absolute;top:550px;left:570px}

/* numbers */
.numbers{top:675px;height:593px;text-align:center}
.section-title{font-size:42px;font-weight:300;color:var(--ink)}
.numbers .section-title{position:absolute;top:62px;width:1200px}
.stats{position:absolute;top:178px;left:150px;width:900px;display:flex;justify-content:space-between}
.stat{width:260px}
.stat svg{height:90px}
.stat-value{font-size:44px;font-weight:300;margin-top:12px}
.stat-label{font-size:15px;font-weight:700;margin-top:8px}
.stat-text{font-size:14px;line-height:1.35;color:#333;margin-top:8px}

/* band */
.band{top:1268px;height:158px;background:var(--dark);color:var(--white);text-align:center}
.band-rule{position:absolute;left:520px;width:160px;height:2px;background:#888}
.band-text{position:absolute;top:46px;left:270px;width:660px;font-size:21px;line-height:1.55}

/* dashboards */
.dashboards{top:1426px;height:432px}
.shot{position:absolute;background:linear-gradient(180deg,#eef1f4,#d8dde3);border:1px solid #ccc}
.shot-one{top:24px;left:290px;width:286px;height:84px}
.shot-two{top:64px;left:604px;width:278px;height:112px}
.dash-title{position:absolute;top:24px;left:590px;font-size:15px;font-weight:500}
.dash-text{position:absolute;top:46px;left:590px;font-size:13px;color:var(--muted)}
.dashboards .section-title{position:absolute;top:320px;width:1200px;text-align:center;font-size:38px}

/* pricing */
.pricing{top:1858px;height:646px;background:linear-gradient(160deg,var(--blue-deep) 0%,#2f94c4 55%,var(--blue-light) 100%)}
.plan{position:absolute;top:64px;width:216px;height:510px;background:var(--white);text-align:center;padding-top:32px}
.plan-name{font-size:20px;font-weight:500;color:#555}
.plan-price{display:flex;justify-content:center;align-items:flex-start;margin-top:4px}
.plan-cur{font-size:18px;margin-top:8px}
.plan-amount{font-size:62px;font-weight:700;line-height:1}
.plan-per{font-size:11px;color:var(--muted);align-self:flex-end;margin:0 0 10px 4px}
.plan-text{font-size:14px;line-height:1.35;color:#444;padding:22px 28px 0;height:250px;overflow:hidden}
.plan-btn{position:absolute;left:52px;bottom:40px;width:112px;height:40px;border-radius:20px;background:var(--blue);color:var(--white);font-size:12px;font-weight:700;display:flex;align-items:center;justify-content:center}

/* contact */
.contact{top:2504px;height:586px;text-align:center}
.contact .section-title{position:absolute;top:42px;width:1200px;font-size:40px}
.contact-lead{position:absolute;top:116px;left:380px;width:440px;font-size:18px;font-weight:300;color:var(--muted);line-height:1.4}
.field-label{position:absolute;font-size:13px;text-align:left}
.field{position:absolute;height:40px;background:var(--field);border:1px solid #eee}
.send{position:absolute;top:475px;left:539px;width:118px;height:38px;border-radius:19px;background:var(--blue);color:var(--white);font-size:14px;font-weight:500;display:flex;align-items:center;justify-content:center}

/* footer */
.site-footer{top:3090px;height:356px;background:var(--darker);color:var(--white)}
.foot-heading{position:absolute;font-size:12px;letter-spacing:1px;text-transform:uppercase}
.foot-brand{position:absolute;top:138px;left:169px;font-size:14px;font-weight:500;text-transform:uppercase}
.foot-links{position:absolute;top:165px;left:169px;list-style:none;font-size:13px;line-height:1.5;color:#ddd}
.foot-news{position:absolute;top:80px;left:388px;width:310px;font-size:14px;line-height:1.4;color:#eee}
.foot-sub{position:absolute;top:78px;left:762px;font-size:13px;color:#ddd}
.sub-field{position:absolute;top:117px;left:762px;width:220px;height:30px;border-radius:15px;background:var(--white);font-size:11px;color:#999;padding:8px 14px}
.sub-btn{position:absolute;top:117px;left:940px;width:112px;height:30px;border-radius:15px;background:var(--blue);font-size:12px;display:flex;align-items:center;justify-content:center}
.social{position:absolute;top:165px;left:762px;display:flex;gap:12px}
.social span{width:14px;height:14px;border-radius:50%;background:#8a8a8a}
.copyright{position:absolute;top:290px;left:169px;font-size:12px;color:#ccc}
</style>
</head>
<body>

<section class="hero">
  <div class="hero-photo" role="img" aria-label="Photo of a team working at laptops around a desk"></div>
  <div class="hero-shade"></div>
  <div class="hero-inner">
    <div class="brand">FernHaven</div>
    <p class="hero-text">Join our community of satisfied customers and become discover our array of products and services. FernHaven have developed a new product that enables your company to make sales via video. Give us a shout!</p>
    <div class="hero-actions">
      <span class="btn btn-primary">Learn more</span>
      <span class="btn btn-ghost">Contact us</span>
    </div>
    <svg class="hero-arrow" width="60" height="50" viewBox="0 0 60 50"><path d="M30 4v40M14 28l16 16 16-16" fill="none" stroke="#fff" stroke-width="3"/></svg>
  </div>
</section>

<section class="numbers">
  <h2 class="section-title">check out our numbers</h2>
  <div class="stats">
    <div class="stat">
      <svg viewBox="0 0 90 90" width="90"><g fill="none" stroke="#2a9fd6" stroke-width="3"><rect x="22" y="8" width="36" height="62" rx="5"/><path d="M34 78c10 6 30 4 36-10l-8-18c-2-4-8-2-7 2"/><path d="M55 40V26c0-4-6-4-6 0v20"/></g></svg>
      <div class="stat-value">50</div>
      <div class="stat-label">adaptive contents</div>
      <p class="stat-text">Lorem ipsum dolor sit amet, consectetur adipiscing elit, sed do eiusmod tempor incididunt ut labore et dolore magna aliqua. Ut enim ad minim veniam, quis nostrud exercitation ullamco laboris nisi ut aliquip ex ea commodo consequat.</p>
    </div>
    <div class="stat">
      <svg viewBox="0 0 90 90" width="90"><g fill="none" stroke="#2a9fd6" stroke-width="3"><rect x="10" y="14" width="70" height="48" rx="3"/><path d="M36 62l-4 14h26l-4-14M26 78h38"/></g></svg>
      <div class="stat-value">28</div>
      <div class="stat-label">prologdashboards</div>
      <p class="stat-text">Lorem ipsum dolor sit amet, consectetur adipiscing elit, sed do eiusmod tempor incididunt ut labore et dolore magna aliqua. Ut enim ad minim veniam, quis nostrud exercitation ullamco laboris nisi ut aliquip ex ea commodo consequat.</p>
    </div>
    <div class="stat">
      <svg viewBox="0 0 90 90" width="90"><g fill="none" stroke="#2a9fd6" stroke-width="3"><path d="M30 18l10 14-6 6c4 8 10 14 18 18l6-6 14 10-6 10c-22 2-46-22-46-46z"/><path d="M56 22a14 14 0 0 1 12 12M58 10a26 26 0 0 1 22 22"/></g></svg>
      <div class="stat-value">24</div>
      <div class="stat-label">24 helpdesk</div>
      <p class="stat-text">Lorem ipsum dolor sit amet, consectetur adipiscing elit, sed do eiusmod tempor incididunt ut labore et dolore magna aliqua. Ut enim ad minim veniam, quis nostrud exercitation ullamco laboris nisi ut aliquip ex ea commodo consequat.</p>
    </div>
  </div>
</section>

<section class="band">
  <div class="band-rule" style="top:24px"></div>
  <p class="band-text">Did you know? with our services, your customers can start a video call to a dealer using a button on your homepage.</p>
  <div class="band-rule" style="top:132px"></div>
</section>

<section class="dashboards">
  <div class="shot shot-one" role="img" aria-label="Screenshot of the video salesroom dashboard"></div>
  <div class="dash-title">Check out our dashboards!</div>
  <div class="dash-text">Lorem ipsum dolor sit amet, consectetur</div>
  <div class="shot shot-two" role="img" aria-label="Screenshot of the call routing rules screen"></div>
  <h2 class="section-title">check out our businesses plans!</h2>
</section>

<section class="pricing">
  <div class="plan" style="left:144px">
    <div class="plan-name">Standard</div>
    <div class="plan-price"><span class="plan-cur">$</span><span class="plan-amount">35</span><span class="plan-per">per month</span></div>
    <p class="plan-text">Lorem ipsum dolor sit amet, consectetur adipiscing elit, sed do eiusmod tempor incididunt ut labore et dolore magna aliqua. Ut enim ad minim veniam, quis nostrud exercitation ullamco laboris nisi ut aliquip ex ea commodo consequat.</p>
    <span class="plan-btn">BUY NOW</span>
  </div>
  <div class="plan" style="left:381px">
    <div class="plan-name">Business</div>
    <div class="plan-price"><span class="plan-cur">$</span><span class="plan-amount">65</span><span class="plan-per">per day</span></div>
    <p class="plan-text">Lorem ipsum dolor sit amet, consectetur adipiscing elit, sed do eiusmod tempor incididunt ut labore et dolore magna aliqua. Ut enim ad minim veniam, quis nostrud exercitation ullamco laboris nisi ut aliquip ex ea commodo consequat.</p>
    <span class="plan-btn">BUY NOW</span>
  </div>
  <div class="plan" style="left:618px">
    <div class="plan-name">Premium</div>
    <div class="plan-price"><span class="plan-cur">$</span><span class="plan-amount">90</span><span class="plan-per">per month</span></div>
    <p class="plan-text">Lorem ipsum dolor sit amet, consectetur adipiscing elit, sed do eiusmod tempor incididunt ut labore et dolore magna aliqua. Ut enim ad minim veniam, quis nostrud exercitation ullamco laboris nisi ut aliquip ex ea commodo consequat.</p>
    <span class="plan-btn">BUY NOW</span>
  </div>
  <div class="plan" style="left:855px">
    <div class="plan-name">Ultimate</div>
    <div class="plan-price"><span class="plan-cur">$</span><span class="plan-amount">150</span><span class="plan-per">per year</span></div>
    <p class="plan-text">Lorem ipsum dolor sit amet, consectetur adipiscing elit, sed do eiusmod tempor incididunt ut labore et dolore magna aliqua. Ut enim ad minim veniam, quis nostrud exercitation ullamco laboris nisi ut aliquip ex ea commodo consequat.</p>
    <span class="plan-btn">BUY NOW</span>
  </div>
</section>

<section class="contact">
  <h2 class="section-title">CONTACT US</h2>
  <p class="contact-lead">Easily add subscribe and contact forms without any server-side integration.</p>
  <span class="field-label" style="top:198px;left:305px">Name</span>
  <span class="field-label" style="top:198px;left:507px">Email</span>
  <span class="field-label" style="top:198px;left:708px">Phone</span>
  <div class="field" style="top:222px;left:305px;width:180px"></div>
  <div class="field" style="top:222px;left:507px;width:180px"></div>
  <div class="field" style="top:222px;left:708px;width:180px"></div>
  <span class="field-label" style="top:282px;left:305px">Message</span>
  <div class="field" style="top:306px;left:305px;width:583px;height:145px"></div>
  <span class="send">SEND</span>
</section>

<footer class="site-footer">
  <div class="foot-heading" style="top:48px;left:388px">Recent news</div>
  <div class="foot-heading" style="top:48px;left:762px">Subscribe</div>
  <div class="foot-brand">FernHaven</div>
  <ul class="foot-links"><li>About Us</li><li>Services</li><li>Selected Work</li><li>Get In Touch</li></ul>
  <p class="foot-news">Lorem ipsum dolor sit amet, consectetur adipiscing elit, sed do eiusmod tempor incididunt ut labore et dolore magna aliqua. Ut enim ad minim veniam, quis nostrud exercitation ullamco laboris nisi ut aliquip ex ea commodo consequat.</p>
  <p class="foot-sub">Get monthly updates and free resources.</p>
  <div class="sub-field">Email</div>
  <span class="sub-btn">Subscribe</span>
  <div class="social"><span></span><span></span><span></span><span></span><span></span><span></span></div>
  <p class="copyright">© FERNHAVEN – All Rights Reserved</p>
</footer>

</body>
</html>
```